Design for Corporate Desktop Background

We are looking for a desktop design that is a dark in color probably blue that our employees will see on a daily basis. Professional and incorporates our logo. Might have some of our vehicles in it and or a night time city picture. All attached are samples...we are looking for new ideas. A few messages we'd like to convey to our employees that will be viewing the background daily subtly (watermarks?) are:
Safety
You are valued
Family
Honesty
Integrity
Perseverance
Respect
Sustainability
Learning thru Reflection

Target Market(s)

Message to our own employees....commit to company. Enjoy your work....make a difference.

Industry/Entity Type

It Professional

Number of Pages Required

1 page

Colors
0355a3
000000
1b1b1b
333333
474747

Requirements
Must have
• Positive message to employees
• Customer Service....
• Make a difference
• see our website....www.glowtendpro.com
Nice to have
• Cut waste
• Stop unsafe behavior
• Expect excellence

```html
<!DOCTYPE html>
<html lang="en">
<head>
<meta charset="utf-8">
<title>GlowTend Pro – Our Values</title>
<link rel="stylesheet" href="https://fonts.googleapis.com/css2?family=Libre+Baskerville:ital,wght@0,700;1,400&family=Roboto+Condensed:wght@700&display=swap">
<style>
  :root {
    --navy-deep: #050f33;
    --navy: #0a1a4f;
    --city-grey: #3b3b3b;
    --city-dark: #1b1b1b;
    --value-red: #f20a1c;
    --value-blue: #17248c;
    --value-charcoal: #333333;
    --value-black: #1c1c1c;
    --hex-edge: #6c7183;
    --ink-white: #ffffff;
  }
  * { margin: 0; padding: 0; box-sizing: border-box; }
  html, body { width: 1200px; height: 848px; overflow: hidden; background: var(--navy-deep); }
  .wallpaper { position: relative; width: 1200px; height: 848px; overflow: hidden; }
  .city-backdrop {
    position: absolute; inset: 0;
    background:
      radial-gradient(circle at 780px 280px, rgba(255,255,255,.18), transparent 140px),
      linear-gradient(90deg, var(--navy-deep) 0%, var(--navy) 38%, #1d2235 58%, var(--city-grey) 78%, #2b2b2b 100%);
  }
  .values-grid { position: absolute; inset: 0; }
  .value-label {
    font-family: "Libre Baskerville", Georgia, serif;
    font-weight: 700; fill: var(--ink-white); letter-spacing: 1px;
  }
  .brand-name {
    position: absolute; top: 46px; right: 30px; width: 300px;
    font-family: "Libre Baskerville", Georgia, serif; font-weight: 700;
    font-size: 40px; line-height: 46px; color: var(--value-red);
    text-align: center; text-transform: uppercase; letter-spacing: 1px;
  }
  .website-band { position: absolute; inset: 0; }
  .website-cta {
    position: absolute; left: 890px; top: 778px; width: 292px; text-align: center; color: var(--ink-white);
  }
  .website-cta .cta-lead { font-family: "Libre Baskerville", Georgia, serif; font-style: italic; font-size: 16px; letter-spacing: 1px; }
  .website-cta .cta-url { font-family: "Roboto Condensed", Arial, sans-serif; font-weight: 700; font-size: 19px; letter-spacing: 1px; margin-top: 4px; }
</style>
</head>
<body>
<main class="wallpaper">
  <div class="city-backdrop" role="img" aria-label="Night-time city street photograph with tram tracks and glowing street lights, fading into deep navy on the left"></div>

  <svg class="values-grid" width="1200" height="848" viewBox="0 0 1200 848" aria-label="Company values">
    <!-- Respect -->
    <polygon points="144,97 226,144 226,238 144,285 62,238 62,144" fill="var(--value-blue)" stroke="#1a2560" stroke-width="8"/>
    <text class="value-label" x="144" y="200" text-anchor="middle" font-size="24">RESPECT</text>

    <!-- Sustainability -->
    <polygon points="252,144 333,97 423,144 513,97 598,144 598,238 513,285 423,238 333,285 252,238" fill="var(--value-red)" stroke="var(--hex-edge)" stroke-width="7"/>
    <text class="value-label" x="423" y="201" text-anchor="middle" font-size="27">SUSTAINABILITY</text>

    <!-- Safety / Honesty / Family -->
    <polygon points="243,260 325,307 325,399 243,446 161,399 161,307" fill="var(--value-charcoal)"/>
    <text class="value-label" x="237" y="366" text-anchor="middle" font-size="24">SAFETY</text>
    <polygon points="422,260 504,307 504,399 422,446 340,399 340,307" fill="var(--value-blue)"/>
    <text class="value-label" x="422" y="362" text-anchor="middle" font-size="24">HONESTY</text>
    <polygon points="602,260 684,307 684,399 602,446 520,399 520,307" fill="var(--value-red)"/>
    <text class="value-label" x="602" y="362" text-anchor="middle" font-size="24">FAMILY</text>

    <!-- Learning / Valued / Integrity -->
    <polygon points="333,427 415,474 415,566 333,613 251,566 251,474" fill="var(--value-red)"/>
    <text class="value-label" text-anchor="middle" font-size="19" letter-spacing="0">
      <tspan x="330" y="497">LEARNING</tspan>
      <tspan x="330" y="521">THROUGH</tspan>
      <tspan x="333" y="545">REFLECTION</tspan>
    </text>
    <polygon points="514,421 600,470 600,566 514,615 428,566 428,470" fill="var(--navy-deep)" stroke="var(--hex-edge)" stroke-width="6"/>
    <text class="value-label" text-anchor="middle" font-size="23">
      <tspan x="516" y="513">YOU ARE</tspan>
      <tspan x="512" y="538">VALUED</tspan>
    </text>
    <polygon points="700,421 786,470 786,566 700,615 614,566 614,470" fill="var(--value-blue)" stroke="var(--hex-edge)" stroke-width="6"/>
    <text class="value-label" x="701" y="526" text-anchor="middle" font-size="23">INTEGRITY</text>

    <!-- Perseverance -->
    <polygon points="154,627 241,581 330,627 419,581 506,627 506,728 419,776 330,728 241,776 154,728" fill="var(--value-black)" stroke="var(--hex-edge)" stroke-width="7"/>
    <text class="value-label" x="330" y="688" text-anchor="middle" font-size="27" letter-spacing="2">PERSEVARANCE</text>
  </svg>

  <div class="brand-name">GlowTend Pro</div>

  <svg class="website-band" width="1200" height="848" viewBox="0 0 1200 848" aria-hidden="true">
    <polygon points="833,838 906,768 1200,768 1200,848 833,848" fill="var(--value-red)"/>
    <rect x="0" y="838" width="1200" height="10" fill="var(--value-red)"/>
  </svg>
  <div class="website-cta">
    <div class="cta-lead">Visit Our Website:</div>
    <div class="cta-url">www.glowtendpro.com</div>
  </div>
</main>
</body>
</html>
```